Vehicle Wrap Design

I have a Korvane KT310 with 2 side doors and need a wrap designing for a laundry business. Main colours are green and blue
Attached are some similar designs to what I like along with our logo. the softwash logo is a service we are offering.
I want the following bit of information on the van:
FREE PICKUP AND DELIVERY
1 HOUR VIP SERVICE
20% OFF YOUR 1ST ORDER
NEXT GENERATION DRY CLEANING
WASH & FOLD SERVICE
www.brookvalewash.services
47 615 938
Colors
33b8a4
33a6d7

```html
<!DOCTYPE html>
<html lang="en">
<head>
<meta charset="utf-8">
<title>Brookvale Wash Services – Van Wrap</title>
<link href="https://fonts.googleapis.com/css2?family=Oswald:wght@400;500&display=swap" rel="stylesheet">
<style>
  :root {
    --backdrop: #eef1f4;
    --sky: #a9daf3;
    --sky-pale: #d6eefa;
    --navy: #0f4f95;
    --deep: #0b3f7a;
    --blue: #33a6d7;
    --brand-blue: #1779c3;
    --green: #1a9a6a;
    --teal: #33b8a4;
    --ink: #1b2433;
    --bullet-text: #8fd3f5;
  }
  html, body {
    margin: 0;
    padding: 0;
    width: 1200px;
    height: 779px;
    overflow: hidden;
    background: var(--backdrop);
  }
  .wrap-artwork {
    display: block;
    width: 1200px;
    height: 779px;
  }
  .service-list text {
    font-family: "Oswald", sans-serif;
    font-weight: 500;
    font-size: 15.5px;
    fill: var(--bullet-text);
    letter-spacing: 0.2px;
  }
  .service-list circle { fill: var(--blue); }
  .brand-name {
    font-family: "Oswald", sans-serif;
    font-weight: 400;
    fill: var(--brand-blue);
  }
  .partner-name {
    font-family: "Oswald", sans-serif;
    font-weight: 500;
    fill: var(--blue);
  }
  .contact text {
    font-family: "Oswald", sans-serif;
    font-weight: 400;
    fill: var(--ink);
  }
  .contact .icon { fill: none; stroke: var(--ink); stroke-width: 1.6; }
</style>
</head>
<body>
<svg class="wrap-artwork" viewBox="0 0 1200 779" xmlns="http://www.w3.org/2000/svg">
  <defs>
    <clipPath id="panel-clip">
      <rect x="110" y="215" width="975" height="385" rx="26"/>
    </clipPath>
    <linearGradient id="sky-fade" x1="0" y1="0" x2="0" y2="1">
      <stop offset="0" stop-color="#9fd4f1"/>
      <stop offset="0.55" stop-color="#cbe9f8"/>
      <stop offset="1" stop-color="#e4f4fc"/>
    </linearGradient>
    <linearGradient id="laundry-tones" x1="0" y1="0" x2="1" y2="1">
      <stop offset="0" stop-color="#e9f3fa"/>
      <stop offset="0.5" stop-color="#c9dfe8"/>
      <stop offset="1" stop-color="#c9a66a"/>
    </linearGradient>
  </defs>

  <g class="wrap-panel" clip-path="url(#panel-clip)">
    <rect class="panel-base" x="110" y="215" width="975" height="385" fill="url(#sky-fade)"/>

    <!-- top navy sweep holding the service list -->
    <path class="top-sweep" d="M600,215 L1010,215 C960,250 930,300 890,335 C840,375 720,392 600,394 Z" fill="var(--navy)"/>
    <path class="top-sweep-line" d="M600,401 C720,399 840,383 897,343 C937,311 967,263 1022,222" fill="none" stroke="var(--deep)" stroke-width="3"/>
    <path class="top-sweep-accent" d="M600,407 C720,405 850,390 907,350" fill="none" stroke="var(--teal)" stroke-width="3"/>

    <!-- lower waves -->
    <path class="wave-blue" d="M300,485 C420,520 560,545 720,525 C860,505 960,455 1085,440 L1085,600 L300,600 Z" fill="var(--navy)"/>
    <path class="wave-contact-band" d="M330,520 C450,528 580,530 700,522 C800,515 880,495 960,470 L960,490 C860,525 760,560 640,585 C540,592 430,588 360,580 Z" fill="var(--sky-pale)"/>
    <path class="wave-green-body" d="M690,495 C810,462 960,432 1085,428 L1085,480 C980,488 880,525 790,560 C760,575 735,590 720,600 L640,600 C660,560 670,520 690,495 Z" fill="var(--green)"/>
    <path class="wave-teal-right" d="M960,445 C1010,436 1050,432 1085,432 L1085,600 L1040,600 C1040,540 1010,480 960,445 Z" fill="var(--blue)"/>
    <path class="wave-dark-line" d="M330,512 C450,522 590,522 720,510 C850,496 960,462 1085,452" fill="none" stroke="#0b1c2e" stroke-width="4"/>
    <path class="wave-dark-line" d="M360,590 C520,598 700,572 960,496 C1010,484 1050,480 1085,478" fill="none" stroke="#0b1c2e" stroke-width="3"/>
  </g>

  <!-- services -->
  <g class="service-list">
    <circle cx="658" cy="268" r="4"/><text x="667" y="274">NEXT GENERATION DRY CLEANING</text>
    <circle cx="658" cy="284" r="4"/><text x="667" y="290">FREE PICKUP AND DELIVERY</text>
    <circle cx="658" cy="300" r="4"/><text x="667" y="306">20% OFF YOUR 1ST ORDER</text>
    <circle cx="658" cy="316" r="4"/><text x="667" y="322">WASH &amp; FOLD SERVICE</text>
    <circle cx="658" cy="332" r="4"/><text x="667" y="338">1 HOUR VIP SERVICE</text>
  </g>

  <!-- main brand name -->
  <g class="brand-block" transform="translate(730,462) rotate(-22)">
    <text class="brand-name" x="0" y="0" font-size="76">brookvale</text>
    <text class="brand-name" x="36" y="38" font-size="27" letter-spacing="6">wash services</text>
  </g>

  <!-- partner service name -->
  <g class="partner-block">
    <circle cx="304" cy="412" r="15" fill="var(--green)"/>
    <text class="partner-name" x="220" y="455" font-size="32">Puravel</text>
    <text class="partner-name" x="220" y="474" font-size="13" letter-spacing="4">WET CLEANING</text>
  </g>

  <!-- laundry basket image area -->
  <rect class="laundry-photo" role="img" aria-label="Basket of folded towels with daisies" x="392" y="405" width="178" height="92" rx="10" fill="url(#laundry-tones)"/>

  <!-- contact -->
  <g class="contact">
    <g class="icon" transform="translate(402,539)">
      <circle r="8"/>
      <ellipse rx="3.5" ry="8"/>
      <line x1="-8" y1="0" x2="8" y2="0"/>
    </g>
    <text x="415" y="547" font-size="22">www.brookvalewash.services</text>
    <path class="icon" d="M458,556 c-3,2 -3,10 0,14 l3,-1 -1,-4 -2,0 c-1,-2 -1,-4 0,-5 l2,0 1,-4 z"/>
    <text x="468" y="574" font-size="24">47 615 938</text>
  </g>
</svg>
</body>
</html>
```